Business Card design for a skin clinic

i would like a business card design for our skin clinic.
our logo colors are Blue and Grey and Bule /white.
we are searching for a minimalistic design yet very elegant,dynamic and professional which can reflect a professional medical skin care clinic( not a beauty salon).
THE DESGIN IS NOT FOR A PERSON IT WILL BE USED IN THE CLINIC FOR CLIENTS SO THERE SHOULD BE NO NAME OF A PERSON ONLY THE CLINIC NAME AND THE CONTACT INFO

Target Market(s)
young and old womens
Industry/Entity Type
Business
Contact Information for Business Card
we have 2 address and both should be on the card.
address A: Lindenhoflaan 214B, 3041KP Rotterdam, Tel 010 483 21 95
address B: Zonnewijzerstraat 238, 1062RT Amsterdam Tel 020 571 3829
website www.huidpuntzorg.nu, email info@huidpuntzorg.nu
Look and feel
Each slider illustrates characteristics of the customer's brand and the style your logo design should communicate.

```html
<!DOCTYPE html>
<html lang="nl">
<head>
<meta charset="utf-8">
<title>Huidpuntzorg – visitekaartje</title>
<link rel="stylesheet" href="https://fonts.googleapis.com/css2?family=Didact+Gothic&family=Questrial&display=swap">
<style>
  :root {
    --page: #e9e7e3;
    --card: #3b4048;
    --card-deep: #33373e;
    --portrait-light: #5a5d63;
    --portrait-warm: #6a6663;
    --brand-blue: #3a8fd6;
    --ink-light: #f2f3f5;
    --ink-soft: #c9ccd1;
  }
  html, body {
    margin: 0;
    width: 1200px;
    height: 902px;
    overflow: hidden;
    background: var(--page);
  }
  .stage {
    position: relative;
    width: 1200px;
    height: 902px;
  }
  .business-card {
    position: absolute;
    left: 150px;
    top: 160px;
    width: 900px;
    height: 582px;
    background: linear-gradient(135deg, var(--card) 0%, var(--card-deep) 100%);
    border-radius: 6px;
    box-shadow: 0 18px 40px rgba(0,0,0,0.25);
    overflow: hidden;
  }
  .portrait-area {
    position: absolute;
    right: 0;
    top: 0;
    width: 460px;
    height: 100%;
    background: radial-gradient(ellipse at 45% 40%, var(--portrait-warm) 0%, var(--portrait-light) 35%, rgba(59,64,72,0) 75%);
    opacity: 0.75;
  }
  .brand {
    position: absolute;
    left: 270px;
    top: 230px;
    display: flex;
    align-items: center;
    gap: 18px;
  }
  .brand-dot {
    width: 26px;
    height: 26px;
    border-radius: 50%;
    background: var(--brand-blue);
  }
  .brand-name {
    font-family: "Didact Gothic", sans-serif;
    font-size: 54px;
    letter-spacing: 7px;
    color: var(--ink-light);
    line-height: 1;
  }
  .tagline {
    position: absolute;
    left: 318px;
    top: 306px;
    font-family: "Didact Gothic", sans-serif;
    font-size: 25px;
    letter-spacing: 5px;
    color: var(--ink-soft);
  }
  .website {
    position: absolute;
    right: 60px;
    bottom: 70px;
    font-family: "Questrial", sans-serif;
    font-size: 26px;
    letter-spacing: 1px;
    color: var(--ink-light);
  }
</style>
</head>
<body>
  <main class="stage">
    <section class="business-card">
      <div class="portrait-area" role="img" aria-label="Soft-toned portrait of a woman with clear skin, hand resting at her chin"></div>
      <div class="brand">
        <span class="brand-dot"></span>
        <span class="brand-name">HUIDPUNTZORG</span>
      </div>
      <p class="tagline">next generation skin care</p>
      <p class="website">www.huidpuntzorg.nu</p>
    </section>
  </main>
</body>
</html>
```